Law firm Seeks Modern and Engaging Site Redesign

Law firm seeks a new web site. Should be modern, but retaining existing logo. Needs to include contact section, professional bio, services offered, and contact information.

The site should be modern, responsive, and able to be SEO optimized.

The finished product should be coded in a Wordpress site, which I will provide. I can work with other platforms, including Wix, but WP is preferred.

Note the current site is https://www.tallowfieldlaw.example/#/home

Target Market(s)

Family Law Practice

Industry/Entity Type

Legal

Coding

Coded - Design and coding required

Number of Pages Required

4 page

Font styles to use
Sans Serif

Requirements
Must have
• Service description
Bio pages for partners
Contact Form
Awards/Publication page

```html
<!DOCTYPE html>
<html lang="en">
<head>
<meta charset="utf-8">
<title>Tallowfield Marsh | Attorneys at Law</title>
<link rel="stylesheet" href="https://fonts.googleapis.com/css2?family=Open+Sans:wght@300;400;600&display=swap">
<style>
:root{
  --blue:#4d6fd1;
  --band:#4a60a3;
  --ink:#333;
  --muted:#888;
  --beige:#f2ebe1;
  --footer:#151515;
  --white:#fff;
}
*{margin:0;padding:0;box-sizing:border-box}
html,body{width:1200px;height:3441px;overflow:hidden}
body{position:relative;font-family:'Open Sans',sans-serif;color:var(--ink);background:var(--white)}
.abs{position:absolute}
.label{font-size:12px;letter-spacing:2px;color:var(--blue);font-weight:600;text-transform:uppercase}
.h2{font-size:33px;font-weight:400;color:var(--ink);line-height:1.4}
.small{font-size:11px;color:var(--muted);font-weight:300;line-height:20px}
/* header */
.site-header{top:0;left:0;width:1200px;height:78px;background:var(--white)}
.brand{left:104px;top:16px;display:flex;align-items:center;gap:10px}
.brand-mark{width:8px;height:30px;background:var(--blue)}
.brand-name{font-size:26px;color:#5a6f9e;line-height:30px}
.brand-tag{position:absolute;left:18px;top:32px;font-size:10px;color:var(--blue);white-space:nowrap}
.nav{right:99px;top:30px;display:flex;gap:37px;font-size:11px;letter-spacing:1px;color:#555}
.nav .active{color:var(--blue)}
/* hero */
.hero{top:78px;left:0;width:1200px;height:496px;background:linear-gradient(90deg,#3b3d44 0%,#6b5a4e 35%,#8a7566 60%,#3c3c3e 100%)}
.hero-rule{left:513px;top:214px;width:2px;height:220px;background:rgba(255,255,255,.25)}
.hero-rule::after{content:"";position:absolute;left:0;bottom:0;width:2px;height:75px;background:var(--blue)}
.hero-title{left:570px;top:212px;font-size:40px;font-weight:300;color:var(--white);line-height:56px;letter-spacing:1px}
.hero-btn{left:570px;top:366px;width:202px;height:54px;border:2px solid var(--white);border-radius:27px;color:var(--white);font-size:15px;display:flex;align-items:center;justify-content:center}
.dot{top:518px;width:12px;height:12px;border-radius:50%;border:2px solid var(--white)}
/* practice */
.icon-circle{border-radius:50%;background:var(--beige);display:flex;align-items:center;justify-content:center}
.area-title{font-size:17px;letter-spacing:1px;color:var(--ink)}
/* overview */
.photo{display:block}
.para{font-size:11px;color:var(--muted);font-weight:300;line-height:20px}
.link{color:var(--blue);font-size:14px;border-bottom:2px solid var(--blue);padding-bottom:1px}
/* facts */
.facts{top:1226px;left:0;width:1200px;height:264px;background:linear-gradient(90deg,#2b2623,#5a4e45 40%,#3e352f 70%,#2a2522)}
/* why */
.why-title{font-size:17px;letter-spacing:1px;color:var(--ink);text-align:right}
/* attorneys */
.atty-name{font-size:19px;color:var(--ink)}
.atty-more{font-size:14px;color:var(--blue)}
/* newsletter */
.newsletter{top:2942px;left:0;width:1200px;height:115px;background:var(--band)}
/* footer */
.site-footer{top:3057px;left:0;width:1200px;height:384px;background:var(--footer)}
.f-head{font-size:17px;color:var(--white)}
.f-text{font-size:11px;color:#aaa;line-height:20px}
.f-link{font-size:12px;color:#9aa6c9;line-height:23px}
.social{width:26px;height:26px;border-radius:50%;background:#2c2c2c}
</style>
</head>
<body>

<header class="site-header abs">
  <div class="brand abs">
    <div class="brand-name">Tallowfield Marsh</div>
  </div>
  <div class="brand-tag abs" style="left:226px;top:52px">Attorneys at Law</div>
  <nav class="nav abs">
    <span class="active">HOME</span><span>ABOUT</span><span>ATTORNEYS</span><span>FAMILY LAW</span><span>CRIMINAL LAW</span><span>AWARDS</span><span>CONTACT</span>
  </nav>
</header>

<section class="hero abs" role="img" aria-label="Photo of two people shaking hands across a desk"></section>
<div class="hero-rule abs"></div>
<h1 class="hero-title abs">ATTORNEYS FIGHTING FOR<br>YOUR FREEDOM</h1>
<div class="hero-btn abs">Make an Appointment</div>
<div class="dot abs" style="left:583px;background:var(--white)"></div>
<div class="dot abs" style="left:603px"></div>

<!-- practice areas -->
<div class="label abs" style="left:124px;top:661px">Practice Areas</div>
<h2 class="h2 abs" style="left:124px;top:682px;line-height:47px">We serve the best<br>service</h2>

<div class="icon-circle abs" style="left:458px;top:658px;width:94px;height:94px">
  <svg width="48" height="48" viewBox="0 0 48 48" fill="none" stroke="#4d6fd1" stroke-width="2">
    <circle cx="16" cy="12" r="6"/><circle cx="32" cy="12" r="6"/>
    <path d="M6 30c0-7 4-11 10-11s8 3 8 3 2-3 8-3 10 4 10 11"/>
    <circle cx="24" cy="30" r="5"/><path d="M15 46c0-6 4-9 9-9s9 3 9 9"/>
  </svg>
</div>
<div class="area-title abs" style="left:575px;top:660px">FAMILY LAW</div>
<p class="small abs" style="left:575px;top:691px;width:200px">Even the all-powerful Pointing has no control about the blind texts it is an almost unorthographic.</p>

<div class="icon-circle abs" style="left:803px;top:658px;width:94px;height:94px">
  <svg width="48" height="48" viewBox="0 0 48 48" fill="none" stroke="#4d6fd1" stroke-width="2">
    <rect x="5" y="5" width="38" height="38"/><path d="M5 11h38M13 11v32M21 11v32M27 11v32M35 11v32"/>
  </svg>
</div>
<div class="area-title abs" style="left:919px;top:660px">CRIMINAL LAW</div>
<p class="small abs" style="left:919px;top:691px;width:200px">Even the all-powerful Pointing has no control about the blind texts it is an almost unorthographic.</p>

<!-- overview -->
<div class="photo abs" style="left:99px;top:887px;width:469px;height:263px;background:linear-gradient(90deg,#cfd2d6,#b9bcc0 70%,#5b4a3d)" role="img" aria-label="Photo of the two founding partners standing in the office lobby"></div>
<div class="label abs" style="left:603px;top:909px">Company Overview</div>
<h2 class="h2 abs" style="left:603px;top:928px">Who We Are</h2>
<p class="para abs" style="left:603px;top:996px;width:518px">The law firm of Tallowfield Marsh, LLC is based in Alder County, conveniently located in Millbrook, New Jersey in 40 Cedar Commons. We serve the needs of clients throughout Alder County, as well as, clients from several other counties, including, but not limited to, Ashford, Linden, Essex and Harbor. Between our partners, we have over 30+ years of experience assisting clients with all of their family law and criminal law needs.</p>
<span class="link abs" style="left:603px;top:1114px">Learn More ›</span>

<!-- facts -->
<section class="facts abs" role="img" aria-label="Photo of courthouse columns"></section>
<div class="abs" style="left:124px;top:1315px;font-size:12px;letter-spacing:2px;color:#ddd">SOME</div>
<div class="abs" style="left:124px;top:1337px;font-size:33px;color:var(--white)">Interesting Facts</div>
<div class="abs" style="left:565px;top:1320px;width:100px;text-align:center;font-size:38px;color:var(--white)">457</div>
<div class="abs" style="left:535px;top:1382px;width:160px;text-align:center;font-size:15px;color:#ddd">Trusted clients</div>

<!-- why -->
<div class="label abs" style="right:604px;top:1578px">The People We Help</div>
<h2 class="h2 abs" style="right:604px;top:1598px">Why We Are</h2>

<div class="why-title abs" style="right:702px;top:1689px">FIGHT FOR JUSTICE</div>
<p class="small abs" style="right:702px;top:1722px;width:340px;text-align:right">Lorem Ipsum is simply dummy text of the printing and typesetting industry.</p>
<div class="why-title abs" style="right:702px;top:1815px">BEST CASE STRATEGY</div>
<p class="small abs" style="right:702px;top:1848px;width:340px;text-align:right">Lorem Ipsum is simply dummy text of the printing and typesetting industry.</p>
<div class="why-title abs" style="right:702px;top:1940px">EXPERIENCE ATTORNEYS</div>
<p class="small abs" style="right:702px;top:1973px;width:340px;text-align:right">Lorem Ipsum is simply dummy text of the printing and typesetting industry.</p>

<svg class="abs" style="left:521px;top:1689px" width="74" height="326" viewBox="0 0 74 326">
  <defs>
    <g id="scales" fill="none" stroke="#4d6fd1" stroke-width="1.6">
      <path d="M37 24v26M27 50h20M22 28h30"/>
      <path d="M22 28l-7 13h14z M52 28l-7 13h14z"/>
      <path d="M15 41a7 4 0 0 0 14 0M45 41a7 4 0 0 0 14 0"/>
    </g>
  </defs>
  <circle cx="37" cy="37" r="37" fill="#f2ebe1"/><use href="#scales"/>
  <circle cx="37" cy="162" r="37" fill="#f2ebe1"/><use href="#scales" y="125"/>
  <circle cx="37" cy="288" r="37" fill="#f2ebe1"/><use href="#scales" y="251"/>
</svg>

<div class="abs" style="left:687px;top:1575px;width:433px;height:496px;background:linear-gradient(135deg,#e9ecef,#c9c3bb 55%,#8d7c6c)" role="img" aria-label="Photo of a handshake over a desk with a laptop"></div>
<div class="abs" style="left:687px;top:1575px;width:181px;height:82px;background:var(--white);border:1px solid #ccc">
  <div style="position:absolute;left:0;bottom:0;width:100%;height:26px;background:#f08a1c"></div>
</div>

<!-- attorneys -->
<div class="label abs" style="left:0;width:1200px;text-align:center;top:2205px">Experienced Attorneys</div>
<h2 class="h2 abs" style="left:0;width:1200px;text-align:center;top:2225px">Meet our attorneys</h2>
<p class="small abs" style="left:0;width:1200px;text-align:center;top:2293px">Whether your needs are family or criminal law related, contact Tallowfield Marsh, LLC to schedule a consultation.</p>

<div class="abs" style="left:80px;top:2640px;width:238px;height:47px;background:linear-gradient(90deg,#7a3b35,#9a5a4e)" role="img" aria-label="Photo of attorney Daniel R. Tallowfield"></div>
<div class="abs" style="left:346px;top:2640px;width:240px;height:47px;background:linear-gradient(90deg,#5a3a34,#8a6a5e)" role="img" aria-label="Photo of attorney Owen P. Marsh"></div>
<div class="abs" style="left:613px;top:2640px;width:240px;height:47px;background:linear-gradient(90deg,#3a3a40,#7c7470)" role="img" aria-label="Photo of attorney Lena M. Hartwell"></div>
<div class="abs" style="left:880px;top:2640px;width:240px;height:47px;background:linear-gradient(90deg,#6c6e78,#c8c6c4)" role="img" aria-label="Photo of attorney Sofia J. Valdane"></div>

<div class="atty-name abs" style="left:80px;top:2710px">Daniel R. Tallowfield</div>
<div class="atty-more abs" style="left:80px;top:2741px">Know More</div>
<p class="small abs" style="left:80px;top:2772px;width:240px">Practices in the area of family law, specializing in high conflict matters relating to divorce, custody, equitable distribution, and complex financial issues.</p>

<div class="atty-name abs" style="left:346px;top:2710px">Owen P. Marsh</div>
<div class="atty-more abs" style="left:346px;top:2741px">Know More</div>
<p class="small abs" style="left:346px;top:2772px;width:240px">Mr. Marsh's primary concentration is in the areas of matrimonial, family law, appellate work, juvenile delinquency, criminal, municipal court, residential real estate transactions and wills and estates.</p>

<div class="atty-name abs" style="left:613px;top:2710px">Lena M. Hartwell</div>
<div class="atty-more abs" style="left:613px;top:2741px">Know More</div>
<p class="small abs" style="left:613px;top:2772px;width:240px">Ms. Hartwell focuses her practice on family and divorce law, which includes child custody, child and spousal support, equitable distribution.</p>

<div class="atty-name abs" style="left:880px;top:2710px">Sofia J. Valdane</div>
<div class="atty-more abs" style="left:880px;top:2741px">Know More</div>
<p class="small abs" style="left:880px;top:2772px;width:240px">Sofia J. Valdane, Esq. ("Sofi") is a skilled and experienced litigator specializing in all facets of family and matrimonial law.</p>

<!-- newsletter -->
<section class="newsletter abs"></section>
<div class="abs" style="left:80px;top:2974px;font-size:33px;color:var(--white)">Subcribe to our Newsletter</div>
<div class="abs" style="left:613px;top:2979px;width:251px;height:48px;border:1px solid rgba(255,255,255,.6);color:#e6e9f3;font-size:15px;padding:14px 12px">Enter email address</div>
<div class="abs" style="left:864px;top:2979px;width:256px;height:48px;background:var(--white);color:#222;font-size:15px;display:flex;align-items:center;justify-content:center">Subscribe</div>

<!-- footer -->
<footer class="site-footer abs"></footer>
<div class="f-head abs" style="left:80px;top:3136px">Business Hours</div>
<div class="f-head abs" style="left:369px;top:3136px">Usefull Links</div>
<div class="f-head abs" style="left:613px;top:3136px">Quick Links</div>
<div class="f-head abs" style="left:880px;top:3136px">Reach Us</div>

<div class="f-text abs" style="left:80px;top:3197px;color:#ddd;font-weight:600">Opening Days:</div>
<div class="f-text abs" style="left:80px;top:3232px">Monday – Friday : 9am to 20 pm<br>Saturday : 9am to 17 pm</div>
<div class="f-text abs" style="left:80px;top:3287px;color:#ddd;font-weight:600">Vacations:</div>
<div class="f-text abs" style="left:80px;top:3323px">All Sunday Days All Official Holidays</div>

<div class="f-link abs" style="left:369px;top:3198px">Privacy Policy<br>Cookie Policy<br>Disclaimer<br>Site Map</div>
<div class="social abs" style="left:369px;top:3320px"></div>
<div class="social abs" style="left:411px;top:3320px"></div>
<div class="social abs" style="left:452px;top:3320px"></div>

<div class="f-link abs" style="left:613px;top:3198px">About Us<br>Family Law<br>Criminal Law<br>Our Attorneys<br>FAQ</div>

<svg class="abs" style="left:879px;top:3198px" width="20" height="160" viewBox="0 0 20 160" fill="#fff">
  <path d="M10 1a6 6 0 0 0-6 6c0 5 6 11 6 11s6-6 6-11a6 6 0 0 0-6-6zm0 8.5a2.5 2.5 0 1 1 0-5 2.5 2.5 0 0 1 0 5z"/>
  <path d="M4 55l3-2 3 4-2 2c1 3 3 5 6 6l2-2 4 3-2 3c-8 0-14-6-14-14z"/>
  <rect x="4" y="89" width="13" height="11" rx="1"/><rect x="7" y="85" width="7" height="5" fill="none" stroke="#fff" stroke-width="1.4"/>
  <rect x="3" y="141" width="15" height="11"/><path d="M3 141l7.5 6 7.5-6" fill="none" stroke="#151515" stroke-width="1.4"/>
</svg>
<div class="f-link abs" style="left:918px;top:3195px;line-height:20px">40 Cedar Commons Drive Suite 210<br>Millbrook, NJ 07000</div>
<div class="f-link abs" style="left:918px;top:3249px;color:#ddd">(555) 014-2210</div>
<div class="f-link abs" style="left:918px;top:3283px;color:#ddd">(555) 014-2277</div>
<div class="f-link abs" style="left:918px;top:3331px">info@tallowfieldlaw.example</div>

<div class="abs" style="left:0;width:1200px;top:3400px;text-align:center;font-size:11px;color:#9aa6c9">Copyright ©2020 Tallowfield &amp; Marsh LLC. All rights reserved | Powered by Northpane Studio</div>

</body>
</html>
```